BRIMLOW Pizza and Wraps

We need a website for a new restaurant called BRIMLOW "PIZZA AND WRAPS".
I have attached fonts, background images, logo, images, content etc.
can provide you with what you need to get the website design done fast and easy

I have uploaded more images of the venue and some menu items. let me know if there is anything I need to provide to make your mission clear and easy

Reason: i would like a little time to provide more feedback to designers

Industry/Entity Type

Restaurant

Coding

Coded - Design and coding required

Number of Pages Required

5+ page

Colors

Designer to choose colors to be used in the design.

Requirements
Must have
• PAGES:
• Our Story
• Menu
• Reservations
• Catering & Delivery
• Contact

```html
<!DOCTYPE html>
<html lang="en">
<head>
<meta charset="utf-8">
<title>Brimlow Pizza and Wraps — Menu</title>
<link rel="stylesheet" href="https://fonts.googleapis.com/css2?family=Questrial&family=Montserrat:wght@600;700&family=Quicksand:wght@400&display=swap">
<style>
  :root {
    --page-bg: #e4e4e0;
    --panel: #ffffff;
    --brand-red: #e42228;
    --ink: #222222;
    --nav-active: #e6e6e4;
    --dot: #b5b5b5;
    --dot-active: #707070;
    --photo-warm: #c98a4a;
    --photo-dark: #6b4a2c;
  }
  * { box-sizing: border-box; margin: 0; padding: 0; }
  html, body { width: 1200px; height: 1000px; overflow: hidden; }
  body { background: var(--page-bg); font-family: "Questrial", "Century Gothic", sans-serif; color: var(--ink); position: relative; }

  .site-header { position: absolute; left: 225px; top: 12px; width: 750px; height: 108px; background: var(--panel); }
  .brand { position: absolute; left: 28px; top: 26px; font-family: "Montserrat", sans-serif; font-weight: 700; font-size: 46px; letter-spacing: 1px; color: var(--brand-red); line-height: 1; }
  .main-nav { position: absolute; left: 300px; top: 38px; display: flex; gap: 0; list-style: none; }
  .main-nav li { font-family: "Montserrat", sans-serif; font-weight: 600; font-size: 10.5px; letter-spacing: .3px; padding: 5px 11px; margin-right: 0; }
  .main-nav li + li { margin-left: 0; }
  .main-nav li.is-active { background: var(--nav-active); }

  .menu-intro { position: absolute; left: 225px; top: 132px; width: 750px; height: 753px; background: var(--panel); }
  .hero-slider { position: absolute; left: 63px; top: 25px; width: 624px; height: 364px;
    background: radial-gradient(ellipse at 40% 80%, #d79a52 0%, var(--photo-warm) 40%, var(--photo-dark) 100%); }
  .slider-arrow { position: absolute; top: 164px; color: #fff; font-size: 22px; font-weight: bold; }
  .slider-arrow.prev { left: 11px; }
  .slider-arrow.next { right: 11px; }
  .slider-dots { position: absolute; left: 337px; top: 404px; display: flex; gap: 6px; }
  .slider-dots span { width: 10px; height: 10px; border-radius: 50%; background: var(--dot); }
  .slider-dots span.is-active { background: var(--dot-active); }

  .section-title { position: absolute; left: 0; width: 750px; top: 446px; text-align: center; font-family: "Quicksand", sans-serif; font-size: 24px; letter-spacing: 3px; color: var(--brand-red); }
  .title-rule { position: absolute; left: 261px; top: 486px; width: 228px; height: 2px; background: var(--brand-red); }
  .intro-copy { position: absolute; left: 150px; width: 450px; top: 516px; text-align: center; font-size: 13px; line-height: 12.6px; }
  .intro-copy p + p { margin-top: 24px; }
  .intro-copy .tagline { margin-top: 24px; }

  .menu-card { position: absolute; top: 898px; height: 120px; background: var(--panel); padding: 26px 50px; }
  .menu-card h2 { font-family: "Montserrat", sans-serif; font-weight: 600; font-size: 18px; line-height: 24px; }
  .menu-card .item-name { margin-top: 16px; font-weight: bold; font-size: 13px; }
  .menu-card .item-desc { font-size: 13px; }
  .menu-card .item-line { margin-top: 16px; font-size: 13px; }
  .card-pizzas { left: 225px; width: 243px; }
  .card-wraps { left: 478px; width: 244px; }
  .card-beverages { left: 731px; width: 244px; }
</style>
</head>
<body>
  <header class="site-header">
    <div class="brand">BRIMLOW</div>
    <ul class="main-nav">
      <li class="is-active">MENU</li>
      <li>OUR STORY</li>
      <li>RESERVATIONS</li>
      <li>CATERING &amp; DELIVERY</li>
      <li>CONTACT</li>
    </ul>
  </header>

  <section class="menu-intro">
    <div class="hero-slider" role="img" aria-label="Wood-fired pizza with olives, onion rings and tomato on baking paper, a bottle and fresh tomatoes behind">
      <span class="slider-arrow prev">&#8249;</span>
      <span class="slider-arrow next">&#8250;</span>
    </div>
    <div class="slider-dots"><span class="is-active"></span><span></span><span></span><span></span><span></span></div>

    <h1 class="section-title">OUR MENU</h1>
    <div class="title-rule"></div>

    <div class="intro-copy">
      <p>Quality food is devotion to seasonal, finest ingredients, and meticulous care in bringing it to life on the plate. At Brimlow, the emphasis is on an experience that extends from a great menu to a relaxed, warm environment of the venue. Choose from our delicious, made from scratch and hand rolled selection of Pizza and Wraps, where our Chefs stand ready to bake it for you on order and straight from our traditional oven to your plate.</p>
      <p>Brimlow promises an unrivalled drinking and dining experience. Our Mediterranean focus is further complemented by a considered variety of beverages and desserts to satisfy your choice of flavours.</p>
      <p class="tagline">Discover Mediterranean tastes &amp; crafted beverages</p>
    </div>
  </section>

  <article class="menu-card card-pizzas">
    <h2>PIZZAS</h2>
    <p class="item-name">Pizza Name, Price</p>
    <p class="item-desc">The description of this</p>
  </article>
  <article class="menu-card card-wraps">
    <h2>WRAPS AND<br>OTHER FOOD</h2>
    <p class="item-name">Wrap Name, Price</p>
  </article>
  <article class="menu-card card-beverages">
    <h2>BEVERAGES</h2>
    <p class="item-line">Beverage 1, price.</p>
  </article>
</body>
</html>
```